Banner Ad Design Project for responsive website

Looking to update the main banner on my website www.vowlantern.example but it will be for our new responsive website, you can see here http://www.vowlantern.example/dev/
Banner should be 300 px high by1920 pix wide
Please contact me with any questions
Should include:
All the text from the existing banner ie
Bridal Show
THE FIRST 50 BRIDES WILL GET A CHANCE TO WIN $25000
Honeymoon Cruise Giveaway
"Pick Your Perfect Gown" casting call
Banner should be 1920 pix wide
Final delivery will require layered psd file and all fonts

Target Market(s)

Brides

Industry/Entity Type

Call

Requirements
Must have
• All the text from the existing banner ie
• Bridal Show
• THE FIRST 50 BRIDES WILL GET A CHANCE TO WIN $25000
• Honeymoon Cruise Giveaway
• "Pick Your Perfect Gown" casting call
• Banner should be 1920 pix wide
Nice to have
• The look and feel of our postcard, see attached
Should not have
• Any specifics to any date/time/location as the banner will be online all the time and the specifics for each show will be different

```html
<!DOCTYPE html>
<html lang="en">
<head>
<meta charset="utf-8">
<title>Bridal Show Banner</title>
<link href="https://fonts.googleapis.com/css2?family=Arimo:ital,wght@0,400;0,700;1,400&family=Great+Vibes&display=swap" rel="stylesheet">
<style>
  :root {
    --stage: #232323;
    --paper: #f4f4f4;
    --paper-shade: #e2e2e2;
    --green: #0f7a1e;
    --green-dark: #0a5a14;
    --blue: #1877c0;
    --band: #4da6ea;
    --band-edge: #a9d6f7;
    --ink: #333333;
    --white: #ffffff;
  }
  * { margin: 0; padding: 0; box-sizing: border-box; }
  html, body { width: 1200px; height: 1000px; overflow: hidden; background: var(--stage); }
  .banner {
    position: absolute; left: 94px; top: 237px; width: 1012px; height: 527px;
    background: radial-gradient(ellipse at 60% 40%, var(--paper) 0%, var(--paper-shade) 100%);
    overflow: hidden; font-family: "Arimo", Arial, sans-serif;
  }
  .banner p, .banner h1 { position: absolute; white-space: nowrap; line-height: 1; }
  .couple-photo {
    position: absolute; left: 0; top: 0; width: 378px; height: 527px;
    background: linear-gradient(160deg, #d9cfc4 0%, #f2ece6 35%, #6f6f74 70%, #e8e8ea 100%);
  }
  .bells { position: absolute; top: 25px; width: 100px; height: 73px; border-radius: 30px;
    background: radial-gradient(ellipse, rgba(15,122,30,0.18), rgba(15,122,30,0)); }
  .bells--left { left: 361px; }
  .bells--right { left: 896px; }
  .show-title {
    left: 466px; top: 20px; width: 430px; text-align: center;
    font-family: "Great Vibes", cursive; font-weight: 400; font-size: 84px; color: var(--green);
  }
  .dice { position: absolute; left: 376px; top: 135px; width: 92px; height: 48px; border-radius: 8px;
    background: linear-gradient(135deg, #6cc0f5, #1f86d6); }
  .prize-intro { right: 18px; top: 127px; font-size: 19px; color: var(--ink); }
  .prize-amount { right: 18px; top: 154px; font-size: 32px; color: var(--blue); font-weight: 700; }
  .casting-band {
    position: absolute; left: 331px; top: 203px; width: 681px; height: 185px;
    background: var(--band); border-top: 3px solid var(--band-edge); border-bottom: 3px solid var(--band-edge);
    color: var(--white);
  }
  .casting-band p { right: 18px; }
  .casting-question { top: 12px; font-size: 19px; }
  .casting-show { top: 44px; font-family: "Great Vibes", cursive; font-size: 58px; line-height: 60px !important; }
  .casting-invite { top: 110px; font-size: 20px; }
  .casting-yes { top: 139px; font-size: 24px; font-weight: 700; }
  .cruise-photo {
    position: absolute; left: 393px; top: 404px; width: 219px; height: 107px;
    border: 3px solid var(--white); border-radius: 4px;
    background: linear-gradient(180deg, #3b8fd3 0%, #a9d3f0 55%, #ffffff 62%, #1b7fb5 80%, #0f5f94 100%);
    box-shadow: 0 1px 3px rgba(0,0,0,0.25);
  }
  .details-button {
    position: absolute; left: 630px; top: 410px; width: 166px; height: 33px;
    background: linear-gradient(180deg, #2f9d3a, var(--green-dark)); border-radius: 3px;
    color: var(--white); font-size: 20px; text-align: center; line-height: 33px;
  }
  .admission { left: 630px; top: 450px; font-size: 26px; font-weight: 700; color: var(--green); }
  .admission sup { font-size: 15px; }
  .cruise-giveaway {
    right: 18px; top: 406px; text-align: right;
    font-family: "Great Vibes", cursive; font-size: 26px; line-height: 34px !important; color: var(--blue);
  }
  .professionals { right: 18px; top: 490px; font-size: 16px; font-style: italic; color: var(--ink); }
</style>
</head>
<body>
  <section class="banner">
    <div class="couple-photo" role="img" aria-label="Photo of a bride and groom embracing, bride holding a bouquet"></div>
    <div class="bells bells--left" role="img" aria-label="Wedding bells ornament"></div>
    <div class="bells bells--right" role="img" aria-label="Wedding bells ornament"></div>
    <h1 class="show-title">Bridal Show</h1>
    <div class="dice" role="img" aria-label="Pair of blue dice"></div>
    <p class="prize-intro">The First 50 Brides will roll the dice for a chance to win</p>
    <p class="prize-amount">$25,000 for your Dream Wedding</p>
    <div class="casting-band">
      <p class="casting-question">Would you like to be the next bride on the BRV program?</p>
      <p class="casting-show">Pick Your Perfect Gown</p>
      <p class="casting-invite">Come to the open casting call at our next bridal show and</p>
      <p class="casting-yes">May be you‘ll be the next bride to say “YES”</p>
    </div>
    <div class="cruise-photo" role="img" aria-label="Photo of a cruise ship on blue sea"></div>
    <div class="details-button">Click for Details</div>
    <p class="admission"><sup>$</sup>8 Admission</p>
    <p class="cruise-giveaway">Plus a Caribbean<br>Cruise Giveaway</p>
    <p class="professionals">Come and meet the area‘s best professionals</p>
  </section>
</body>
</html>
```